Zielgruppe
Wir sind ein Familienweingut in 11. Generation. Durch das lange Bestehen des Betriebes haben wir eine klassische Linie der Weine. Jedoch haben wir neben unserer Classic Linie eine komplett junge und modernere Linie im Weingut wie z.B.: ein Cüvee mit dem Namen 'Wolkentanz' (besteht aus 3 Sorten und ein Bezug zu unseren Freilandschweinen am Weingut wird hergestellt) Durch unsere zwei Produktlinien können wir eine sehr hohe Zielgruppe erreichen. Nun erweitert sich unsere moderne Linie um einen Rosé, dieser soll wie die anderen das jüngere Puplikum ansprechen.
Aufgabenstellung
Wir brauchen ein Etikett für unseren Rose mit dem Namen 'Sky Dash': Pink setzt sich durch die Farbe des Weines zusammen und das Pin-up soll dies verkörpern. Es soll sich ein Pin-up Girl auf dem Etikett befinden, wo auch eine Verbindung zum Wein an sich hergestellt wird. Der Kreativität sind keine Grenzen gesetzt. Auch der Name des Weines muss am Etikett stehen.
Zusätzliche Infos:
Die Maße des Etiketts betragen 113x97mm.
alle weiteren Daten befinden sich bei der Flasche auf dem Rückenetikett; sprich, es geht rein nur um das vordere Etikett und dessen grafische Darstellung.
Danke im Voraus.
Weingut Zwirnlehner

```html
<!DOCTYPE html>
<html lang="de">
<head>
<meta charset="utf-8">
<title>Sky Dash Rosé – Etikett</title>
<link rel="stylesheet" href="https://fonts.googleapis.com/css2?family=Montserrat:wght@400;700&display=swap">
<style>
  :root {
    --page: #ffffff;
    --stripe-light: #ffffff;
    --stripe-grey: #c8c8c8;
    --band-dark: #2c2c2c;
    --band-pink: #f9d4e0;
    --band-cream: #ece8c2;
    --rule-purple: #9a5ba3;
    --glass-blue: #8fd0e4;
    --ink: #2a2a2a;
    --figure-blue: #8cc3dc;
    --figure-skin: #f1d2bf;
    --figure-red: #d9412f;
  }
  * { margin: 0; padding: 0; box-sizing: border-box; }
  html, body {
    width: 1200px;
    height: 1200px;
    overflow: hidden;
    background: var(--page);
  }
  .canvas {
    position: relative;
    width: 1200px;
    height: 1200px;
  }
  .label {
    position: absolute;
    left: 255px;
    top: 141px;
    width: 690px;
    height: 918px;
    overflow: hidden;
  }
  .band { position: absolute; left: 0; width: 100%; }
  .band--stripes {
    top: 0; height: 102px;
    background: repeating-linear-gradient(
      -50deg,
      var(--stripe-light) 0 30px,
      var(--stripe-grey) 30px 34px
    );
  }
  .band--dark-top { top: 102px; height: 31px; background: var(--band-dark); }
  .band--pink-upper { top: 133px; height: 314px; background: var(--band-pink); }
  .rule--upper { top: 447px; height: 10px; background: var(--rule-purple); }
  .band--cream { top: 457px; height: 219px; background: var(--band-cream); }
  .rule--lower { top: 676px; height: 10px; background: var(--rule-purple); }
  .band--pink-lower { top: 686px; height: 199px; background: var(--band-pink); }
  .band--dark-bottom { top: 885px; height: 33px; background: var(--band-dark); }

  .wine-glass {
    position: absolute;
    left: 196px;
    top: 327px;
    width: 51px;
    height: 120px;
  }
  .pinup-figure {
    position: absolute;
    left: 230px;
    top: 51px;
    width: 268px;
    height: 663px;
    border-radius: 120px 120px 40px 40px;
    background: linear-gradient(
      180deg,
      var(--figure-red) 0%,
      var(--figure-skin) 18%,
      var(--figure-blue) 35%,
      var(--figure-blue) 48%,
      var(--figure-skin) 60%,
      var(--figure-skin) 100%
    );
    opacity: 0.85;
  }
  .wine-name {
    position: absolute;
    left: 0;
    width: 100%;
    text-align: center;
    font-family: "Montserrat", sans-serif;
    color: var(--ink);
  }
  .wine-name__title {
    top: 738px;
    font-size: 50px;
    font-weight: 700;
    letter-spacing: 6px;
  }
  .wine-name__type {
    top: 800px;
    font-size: 30px;
    font-weight: 400;
    letter-spacing: 4px;
  }
</style>
</head>
<body>
<main class="canvas">
  <section class="label" aria-label="Etikett Sky Dash Rosé">
    <div class="band band--stripes"></div>
    <div class="band band--dark-top"></div>
    <div class="band band--pink-upper"></div>
    <div class="band rule--upper"></div>
    <div class="band band--cream"></div>
    <div class="band rule--lower"></div>
    <div class="band band--pink-lower"></div>
    <div class="band band--dark-bottom"></div>

    <svg class="wine-glass" viewBox="0 0 51 120" aria-hidden="true">
      <path d="M4 4 H47 L44 38 Q40 62 25.5 64 Q11 62 7 38 Z" fill="none" stroke="var(--glass-blue)" stroke-width="5"/>
      <path d="M8 36 H43 Q40 60 25.5 61 Q11 60 8 36 Z" fill="var(--glass-blue)"/>
      <rect x="23" y="64" width="5" height="44" fill="var(--glass-blue)"/>
      <rect x="8" y="108" width="35" height="8" fill="var(--glass-blue)"/>
    </svg>

    <div class="pinup-figure" role="img" aria-label="Illustration eines Pin-up-Girls mit rotem Kopftuch, blauer Bluse und Shorts, sitzend mit Telefonhörer"></div>

    <h1 class="wine-name wine-name__title">SKY DASH</h1>
    <p class="wine-name wine-name__type">ROSÈ</p>
  </section>
</main>
</body>
</html>
```